Maple Hollow Pet Services ABN 71 493 260 518 needs a Postcard Design

Genuine pet lover offering a professional and highly personalised pet service. I will visit your home daily to care for your pet in their own environment. THE OTHER OPTION FOR WHEN YOU GO ON HOLIDAYS. Dog Holiday Service (includes but not limited to) Feed, Water, Walk, Love & Play. Clean Litter Trays, Hutches & Cages. Administer Medication as Directed. Water Pot Plants & Collec Mail. Individual Dog Walking (Permanent or Casual). REASONABLE RATES. Police Check & References available upon request. Contact HARRIET 0412 684 219

```html
<!DOCTYPE html>
<html lang="en">
<head>
<meta charset="utf-8">
<title>Dog Holiday Service – Postcard</title>
<link href="https://fonts.googleapis.com/css2?family=Yellowtail&family=Marcellus+SC&family=Righteous&display=swap" rel="stylesheet">
<style>
  :root {
    --red: #e31e24;
    --teal: #2cbcbf;
    --teal-light: #a9e0e0;
    --teal-pale: #e3f4f4;
    --ink: #555a5c;
    --white: #ffffff;
    --page: #f2f2f2;
    --rule: #c9c9c9;
  }
  * { box-sizing: border-box; margin: 0; padding: 0; }
  html, body { width: 908px; height: 1200px; overflow: hidden; }
  body { background: var(--page); position: relative; font-family: "Marcellus SC", serif; font-variant: small-caps; }

  .card { position: absolute; width: 706px; height: 546px; background: var(--white); overflow: hidden; box-shadow: 0 2px 8px rgba(0,0,0,.15); }
  .card--front { left: 42px; top: 25px; }
  .card--back { left: 101px; top: 605px; }

  /* Front */
  .hero-photo { position: absolute; inset: 0 0 80px 0;
    background: radial-gradient(ellipse at 45% 55%, #c9a27a 0%, #8a5a3c 18%, #3d4a46 45%, #1f2b2c 100%); }
  .title-rule { position: absolute; left: 55px; right: 55px; height: 2px; background: var(--white); }
  .title-rule--top { top: 23px; left: 57px; right: 57px; }
  .title-rule--mid { top: 88px; }
  .title-rule--low { top: 95px; }
  .title { position: absolute; top: 22px; left: 0; right: 0; text-align: center; white-space: nowrap;
    font-family: "Yellowtail", cursive; font-variant: normal; font-size: 54px; line-height: 64px; font-weight: 400; color: var(--red);
    -webkit-text-stroke: 1.5px var(--white); paint-order: stroke fill; letter-spacing: 1px; }

  .wave { position: absolute; left: 0; bottom: 0; width: 100%; }

  .services { position: absolute; left: 451px; top: 268px; width: 236px; height: 236px; border-radius: 50%;
    border: 2px solid var(--white); padding: 5px; }
  .services__disc { width: 100%; height: 100%; border-radius: 50%; background: var(--red);
    color: var(--white); display: flex; flex-direction: column; align-items: center; justify-content: center;
    text-align: center; transform: rotate(-13deg); line-height: 1.08; }
  .services__disc span { display: block; font-size: 18px; white-space: nowrap; }
  .services__disc .small { font-size: 11px; }

  .contact { position: absolute; display: flex; align-items: center; gap: 8px; white-space: nowrap; }
  .contact--front { left: 42px; top: 478px; }
  .contact__icon { width: 44px; height: 36px; flex: none; }
  .contact__label { font-size: 19px; color: var(--white); }
  .contact__number { font-family: "Righteous", sans-serif; font-variant: normal; font-size: 31px; color: var(--red); letter-spacing: 2px; margin-left: 10px;
    -webkit-text-stroke: 1px var(--white); paint-order: stroke fill; }

  /* Back */
  .dog-lineup { position: absolute; left: 22px; top: 25px; width: 385px; height: 68px;
    background: linear-gradient(90deg, #5a4d45, #d8c7ae 30%, #efe6d6 50%, #b57c52 75%, #8a4f2c); border-radius: 30px 30px 0 0; }
  .intro { position: absolute; left: 18px; top: 90px; width: 392px; min-height: 95px;
    background: var(--teal-pale); border: 2px solid var(--teal); padding: 12px 22px 10px 24px; color: var(--ink); font-size: 12px; line-height: 1.35; }
  .intro p + p { margin-top: 8px; }
  .badge { position: absolute; left: 361px; top: 163px; width: 60px; height: 60px; border-radius: 50%;
    background: var(--red); border: 2px solid var(--white); box-shadow: 0 0 0 1px var(--red);
    color: var(--white); font-size: 8px; line-height: 1.1; display: flex; align-items: center; justify-content: center;
    text-align: center; transform: rotate(-12deg); }
  .assurance { position: absolute; left: 60px; width: 270px; top: 201px; text-align: center; color: var(--red); font-size: 14px; line-height: 1.25; }
  .business { position: absolute; left: 20px; top: 248px; white-space: nowrap; font-family: "Righteous", sans-serif; font-variant: normal; font-size: 15px; color: var(--red); letter-spacing: .2px; }
  .contact-box { position: absolute; left: 18px; top: 273px; width: 388px; height: 45px; border: 2px solid var(--teal); }
  .contact--back { left: 26px; top: 0; height: 41px; gap: 6px; }
  .contact--back .contact__icon { width: 36px; height: 30px; }
  .contact--back .contact__label { color: var(--teal); font-size: 16px; }
  .contact--back .contact__number { color: var(--teal); font-size: 24px; letter-spacing: 1.5px; margin-left: 8px; -webkit-text-stroke: 0; }
  .stamp-box { position: absolute; left: 571px; top: 38px; width: 108px; height: 105px; border: 1.5px solid var(--rule); }
  .address-line { position: absolute; left: 442px; width: 227px; height: 1.5px; background: var(--rule); }
  .paw-trail { position: absolute; left: 40px; top: 424px; width: 440px; height: 70px;
    background: linear-gradient(90deg, rgba(169,224,224,.55), rgba(169,224,224,.25)); border-radius: 20px; }
</style>
</head>
<body>

<section class="card card--front">
  <div class="hero-photo" role="img" aria-label="Photograph of a dog wearing a red knitted scarf in falling snow with candles behind"></div>
  <div class="title-rule title-rule--top"></div>
  <h1 class="title">Dog Holiday Service</h1>
  <div class="title-rule title-rule--mid"></div>
  <div class="title-rule title-rule--low"></div>

  <svg class="wave" width="706" height="120" viewBox="0 0 706 120" aria-hidden="true">
    <path d="M0 12 C200 40 480 45 706 10 V120 H0 Z" fill="var(--teal-light)"/>
    <path d="M0 25 C220 52 480 55 706 28 V120 H0 Z" fill="var(--teal)"/>
    <path d="M0 95 C250 85 470 105 706 92 V120 H0 Z" fill="#5fcfd1" opacity=".6"/>
  </svg>

  <div class="services">
    <div class="services__disc">
      <span>Feed</span>
      <span>Water • Walk</span>
      <span>Love &amp; Play</span>
      <span>Clean Litter Trays</span>
      <span>Hutches &amp; Cages</span>
      <span class="small">Administer Medication as Directed</span>
      <span>Individual Dog Walking</span>
      <span class="small">(Permanent or Casual)</span>
      <span>Water Pot Plants &amp;</span>
      <span>Collec Mail</span>
    </div>
  </div>

  <div class="contact contact--front">
    <svg class="contact__icon" viewBox="0 0 44 36" aria-hidden="true">
      <path d="M2 12 C2 4 42 4 42 12 L38 16 L30 13 L30 9 C24 7 20 7 14 9 L14 13 L6 16 Z" fill="var(--red)"/>
      <path d="M12 16 L32 16 L40 33 L4 33 Z" fill="var(--red)"/>
      <circle cx="22" cy="25" r="6" fill="var(--white)"/>
      <circle cx="22" cy="25" r="3" fill="var(--red)"/>
    </svg>
    <span class="contact__label">Contact Harriet</span>
    <span class="contact__number">0412 684 219</span>
  </div>
</section>

<section class="card card--back">
  <div class="dog-lineup" role="img" aria-label="Row of five dogs peeking over the top of the text panel"></div>
  <div class="intro">
    <p>Genuine pet lover offering a professional and highly personalised pet service.</p>
    <p>I will visit your home daily to care for your pet in their own environment.</p>
  </div>
  <div class="badge">Reasonable<br>Rates!</div>
  <p class="assurance">Police Check &amp; References<br>available upon request!</p>
  <p class="business">MAPLE HOLLOW PET SERVICES ABN 71 493 260 518</p>
  <div class="contact-box">
    <div class="contact contact--back">
      <svg class="contact__icon" viewBox="0 0 44 36" aria-hidden="true">
        <path d="M2 12 C2 4 42 4 42 12 L38 16 L30 13 L30 9 C24 7 20 7 14 9 L14 13 L6 16 Z" fill="var(--teal)"/>
        <path d="M12 16 L32 16 L40 33 L4 33 Z" fill="var(--teal)"/>
        <circle cx="22" cy="25" r="6" fill="var(--white)"/>
        <circle cx="22" cy="25" r="3" fill="var(--teal)"/>
      </svg>
      <span class="contact__label">Contact Harriet</span>
      <span class="contact__number">0412 684 219</span>
    </div>
  </div>

  <div class="stamp-box"></div>
  <div class="address-line" style="top:267px"></div>
  <div class="address-line" style="top:302px"></div>
  <div class="address-line" style="top:337px"></div>

  <div class="paw-trail" role="img" aria-label="Trail of light teal paw prints"></div>

  <svg class="wave" width="706" height="62" viewBox="0 0 706 62" aria-hidden="true">
    <path d="M0 8 C250 0 480 2 706 14 V62 H0 Z" fill="var(--teal-light)"/>
    <path d="M0 14 C260 8 480 12 706 26 V62 H0 Z" fill="var(--teal)"/>
  </svg>
</section>

</body>
</html>
```